Brochure Design - Non-Profit Fundraising Stream

We are a non-profit organization that is developing a fundraising project through the donation of life insurance policies. We have three brochures in each English and French that we developed for a sister organization that we want to reintegrate with our Foundation, keeping the same copy text just changing the logos, colors and make it overall more visually appealing. The foundation is called the 'Varnek-Holt Syndrome Foundation Canada'.
The original files in .docx format are attached as is the full logo and two symbol files. The deliverables would be six documents in total (InDesign or .docx), each brochure in English and French. The color hex codes are:
red: #7b2850
dark blue: #2c79a7
pale blue: #78b2e2

```html
<!DOCTYPE html>
<html lang="en">
<head>
<meta charset="UTF-8">
<title>Unlock the Hidden Value in Your Life Insurance</title>
<link href="https://fonts.googleapis.com/css2?family=Libre+Baskerville:wght@700&family=Source+Sans+3:wght@300;400;600&display=swap" rel="stylesheet">
<style>
  :root {
    --red: #7b2850;
    --dark-blue: #2c79a7;
    --pale-blue: #78b2e2;
    --paper: #f5f4f8;
    --white: #ffffff;
  }
  * { margin: 0; padding: 0; box-sizing: border-box; }
  html, body { width: 927px; height: 1200px; overflow: hidden; background: var(--paper); }
  .brochure {
    position: relative;
    width: 927px;
    height: 1200px;
    overflow: hidden;
    background: var(--paper);
    font-family: "Source Sans 3", sans-serif;
  }
  .side-panel {
    position: absolute;
    left: 636px; top: 0;
    width: 291px; height: 1200px;
    background: var(--dark-blue);
  }
  .foundation-name {
    position: absolute;
    left: 680px; top: 84px;
    width: 220px;
    display: flex;
    align-items: center;
    gap: 10px;
    color: var(--white);
    font-family: "Source Sans 3", sans-serif;
    font-weight: 400;
    font-size: 17px;
    line-height: 1.15;
  }
  .foundation-name .mark {
    flex: 0 0 14px;
    height: 14px;
    border-radius: 50%;
    background: var(--white);
  }
  .eyebrow {
    position: absolute;
    left: 82px; top: 44px;
    color: var(--pale-blue);
    font-weight: 600;
    font-size: 16px;
  }
  .title {
    position: absolute;
    left: 82px; top: 98px;
    color: var(--red);
    font-family: "Libre Baskerville", serif;
    font-weight: 700;
    font-size: 41px;
    line-height: 52px;
    letter-spacing: -0.3px;
  }
  .intro {
    position: absolute;
    left: 82px; top: 217px;
    width: 524px;
    color: var(--dark-blue);
    font-weight: 300;
    font-size: 14.6px;
    line-height: 25.7px;
  }
  .section-heading {
    position: absolute;
    left: 82px;
    color: var(--red);
    font-family: "Libre Baskerville", serif;
    font-weight: 700;
    font-size: 25px;
    line-height: 40px;
  }
  .heading-policies { top: 397px; }
  .heading-advantages { top: 593px; width: 480px; }
  .bullets {
    position: absolute;
    left: 114px;
    width: 490px;
    list-style: none;
    color: var(--dark-blue);
    font-weight: 300;
    font-size: 14px;
    line-height: 30.2px;
  }
  .bullets li { position: relative; padding-left: 10px; }
  .bullets li::before {
    content: "";
    position: absolute;
    left: 0; top: 14px;
    width: 3px; height: 3px;
    border-radius: 50%;
    background: var(--dark-blue);
  }
  .list-policies { top: 448px; }
  .list-advantages { top: 678px; }
  .group-photo {
    position: absolute;
    left: 0; top: 890px;
    width: 636px; height: 310px;
    background: linear-gradient(180deg, rgba(245,244,248,0) 0%, #e9e6e6 22%, #c9b3a6 55%, #8a8d96 100%);
  }
</style>
</head>
<body>
  <main class="brochure">
    <aside class="side-panel"></aside>
    <div class="foundation-name"><span class="mark"></span><span>Varnek-Holt Syndrome Foundation Canada</span></div>

    <p class="eyebrow">For Donors</p>
    <h1 class="title">Unlock the Hidden value<br>In your life insurance</h1>

    <p class="intro">You can maintain or substantially improve your financial position by unlocking the hidden value of your unwanted or unaffordable life insurance via a charitable donation. &nbsp;Every year, seniors over the age of 70 lapse or surrender almost $7 billion of insurance that they might otherwise donate to a charity. You can pay down debt, make major purchases or replenish retirement savings by accessing the value you deserve after paying premiums for decades.</p>

    <h2 class="section-heading heading-policies">Suitable Policies</h2>
    <ul class="bullets list-policies">
      <li>Term, Whole life, Universal or term-to-100 policies</li>
      <li>Insured lives over 70 years old</li>
      <li>In-force greater than 2 years</li>
      <li>Minimum death benefit of $50,000</li>
    </ul>

    <h2 class="section-heading heading-advantages">Advantages of &nbsp;Donating a Life Insurance Policy</h2>
    <ul class="bullets list-advantages">
      <li>You obtain a tax receipt (good for 5 years) for 10%-50% of the face value of the policy (even for term policies that have no “cash surrender value”).</li>
      <li>You convert a “worthless or low cash value policy” into cash in your pocket when you file your income taxes.</li>
      <li>Eliminate the burden of annual premium expenses.</li>
      <li>A Foundation becomes the owner and beneficiary, and it funds the premiums and collects the benefit upon maturity.</li>
    </ul>

    <div class="group-photo" role="img" aria-label="Photo of five smiling young adults standing together against a white brick wall, looking upward"></div>
  </main>
</body>
</html>
```